pvt business card

need clean and modern business card design, possibly two. Logo on front and writing on back-Full source files for logo attached-THE CHOSEN LOGO IS SQUARE PVT with PVT HOLDINGS in ALL BLUE. Please do not use any other logos from files, this is source file that includes correct logo

```html
<!DOCTYPE html>
<html lang="en">
<head>
<meta charset="utf-8">
<title>PVT Holdings business card</title>
<link href="https://fonts.googleapis.com/css2?family=Michroma&family=Lato:wght@400;700&display=swap" rel="stylesheet">
<style>
  :root {
    --bg: #2b2b2b;
    --brand-blue: #3a78c2;
    --card-white: #ffffff;
    --text-dark: #333333;
    --divider: #555555;
  }
  * { margin: 0; padding: 0; box-sizing: border-box; }
  html, body { width: 1200px; height: 895px; overflow: hidden; background: var(--bg); }
  .canvas {
    width: 1200px; height: 895px;
    display: flex; flex-direction: column; align-items: center; justify-content: center;
    gap: 44px;
  }
  .card {
    width: 560px; height: 320px; position: relative; overflow: hidden;
    box-shadow: 0 10px 24px rgba(0,0,0,0.55);
  }
  /* back side */
  .card-back { background: var(--brand-blue); }
  .card-back .back-mark {
    position: absolute; right: 70px; top: 64px;
    display: flex; align-items: center; gap: 10px;
    font-family: "Michroma", sans-serif; font-size: 30px; color: var(--card-white);
    letter-spacing: 2px;
  }
  .back-mark .mark-square { width: 22px; height: 22px; background: var(--card-white); }
  /* front side */
  .card-front { background: var(--card-white); }
  .brand {
    position: absolute; left: 0; right: 0; top: 34px; text-align: center;
    font-family: "Michroma", sans-serif; color: var(--brand-blue);
  }
  .brand-mark { font-size: 40px; letter-spacing: 4px; line-height: 1; padding-left: 60px; }
  .brand-name { font-size: 27px; letter-spacing: 3px; margin-top: 20px; padding-left: 60px; }
  .person {
    position: absolute; top: 174px; right: 305px; text-align: right;
  }
  .person-name {
    font-family: "Michroma", sans-serif; font-size: 17px; color: var(--brand-blue); letter-spacing: 0.5px;
  }
  .person-title {
    font-family: "Lato", sans-serif; font-size: 13px; color: var(--text-dark); margin-top: 2px;
  }
  .divider {
    position: absolute; left: 282px; top: 160px; width: 1px; height: 74px; background: var(--divider);
  }
  .contacts {
    position: absolute; left: 300px; top: 158px; list-style: none;
    font-family: "Lato", sans-serif; font-size: 12.5px; color: var(--text-dark);
  }
  .contacts li { display: flex; align-items: center; gap: 8px; height: 19px; }
  .contacts svg { width: 12px; height: 12px; fill: var(--brand-blue); flex: none; }
  .address-band {
    position: absolute; left: 0; right: 0; top: 254px; height: 34px;
    background: var(--brand-blue); color: var(--card-white);
    font-family: "Lato", sans-serif; font-size: 14px;
    display: flex; align-items: center; justify-content: center; letter-spacing: 0.3px;
  }
</style>
</head>
<body>
<main class="canvas">
  <section class="card card-back" aria-label="Card back">
    <div class="back-mark"><span class="mark-square"></span>PVT</div>
  </section>

  <section class="card card-front" aria-label="Card front">
    <div class="brand">
      <div class="brand-mark">PVT</div>
      <div class="brand-name">PVT HOLDINGS</div>
    </div>

    <div class="person">
      <div class="person-name">DANIEL MARSH</div>
      <div class="person-title">Founder &amp; CEO</div>
    </div>

    <div class="divider"></div>

    <ul class="contacts">
      <li>
        <svg viewBox="0 0 16 16"><path d="M3.5 1l3 3-1.6 1.8c.9 2 2.3 3.4 4.3 4.3L11 8.5l3 3-2 2.5C6.5 13.5 2.5 9.5 1 4z"/></svg>
        000.000.0000
      </li>
      <li>
        <svg viewBox="0 0 16 16"><path d="M4 1h8v4H4zM1 6h14v6h-3v3H4v-3H1zM5 10v4h6v-4z"/></svg>
        999.999.9999
      </li>
      <li>
        <svg viewBox="0 0 16 16"><path d="M1 3h14v1.5L8 9 1 4.5zM1 6.3l7 4.4 7-4.4V13H1z"/></svg>
        dmarsh@pvtholdings.com
      </li>
      <li>
        <svg viewBox="0 0 16 16"><path d="M8 1a7 7 0 100 14A7 7 0 008 1zm0 1.5c.8 0 1.7 1.6 2 4H6c.3-2.4 1.2-4 2-4zM2.6 6.5h2.1c.1-1.5.4-2.8.9-3.6A5.6 5.6 0 002.6 6.5zm8.7 0h2.1a5.6 5.6 0 00-3-3.6c.5.8.8 2.1.9 3.6zM2.6 9.5a5.6 5.6 0 003 3.6c-.5-.8-.8-2.1-.9-3.6zm3.4 0c.3 2.4 1.2 4 2 4s1.7-1.6 2-4zm5.3 0c-.1 1.5-.4 2.8-.9 3.6a5.6 5.6 0 003-3.6z"/></svg>
        www.pvtholdings.com
      </li>
    </ul>

    <div class="address-band">4580 N. Harbor Blvd. Suite B, Linden, California 95236</div>
  </section>
</main>
</body>
</html>
```